Need CATCHY/VIVID Banner design for my new UTV/ATV/Off Road Vehicle turn signal/lighting company

I need a banner ad designed so I can advertise on several different ATV (all terrain vehicle), UTV (Utility Vehicles), Golf Cart and Off-Road Vehicle forums. Ads need to be very catchy and produce a call to action. Action is getting hits to my website. Our main business is selling turn signal kits to make your side by side or your ATV/UTV street legal, as some states now allow you to drive these on public roads if you have the following items: Turn Signals, Horn, Lighted license plate bracket, headlights and brake lights. We sell all of these items for just about any model vehicle out there. Our call to action for this banner would be to get more website visits.

Target Market(s)

Off-road/outdoor enthusiasts,

Industry/Entity Type

Car Accessorie

Font styles to use
Sans Serif

Requirements
Must have
• Ad size need to be either 728x90 or 300x250. Colorful ad with an off-road vehicle integrated to the design (think UTV, side-by-side, etc.
Nice to have
• Nice to haves would be anything that makes this banner ad stand out on very boring web pages.
Should not have
• anything dull

```html
<!DOCTYPE html>
<html lang="en">
<head>
<meta charset="utf-8">
<title>Ridelight Kits – Forum Banner Set</title>
<link href="https://fonts.googleapis.com/css2?family=Saira+Condensed:wght@600;700&family=Saira+Semi+Condensed:ital,wght@0,500;0,700;1,500;1,600&family=Inter:wght@400&display=swap" rel="stylesheet">
<style>
  :root{
    --ink:#1a1a1a;
    --ink-2:#2c2c2c;
    --red:#ec1c24;
    --yellow:#fdc010;
    --white:#ffffff;
    --label:#333333;
    --page:#ffffff;
  }
  *{box-sizing:border-box;margin:0;padding:0}
  html,body{width:1200px;height:974px;overflow:hidden;background:var(--page)}
  .sheet{position:relative;width:1200px;height:974px}
  .size-label{position:absolute;font:400 14px/1 "Inter",sans-serif;color:var(--label)}
  .banner{position:absolute;overflow:hidden;background:var(--ink)}
  .banner > svg.bg{position:absolute;inset:0;width:100%;height:100%}
  .brand{position:absolute;display:flex;align-items:center;gap:7px;
    font:700 20px/1 "Saira Semi Condensed",sans-serif;color:var(--white);letter-spacing:.5px;white-space:nowrap}
  .brand-mark{width:14px;height:14px;background:var(--yellow)}
  .headline{position:absolute;font-family:"Saira Condensed",sans-serif;font-weight:700;color:var(--yellow);white-space:nowrap}
  .headline .light{color:var(--white)}
  .cta{position:absolute;white-space:nowrap}
  .cta-title{display:flex;align-items:center;gap:6px;font:italic 600 30px/1 "Saira Semi Condensed",sans-serif;color:var(--white);letter-spacing:.5px}
  .cta-title::before{content:"›";color:var(--red);font-style:normal;font-size:.8em}
  .cta-sub{font:italic 500 14px/1.1 "Saira Semi Condensed",sans-serif;color:var(--yellow);margin-left:16px}
  .vehicle-photo{position:absolute;border-radius:6px;
    background:linear-gradient(160deg,#3a3a3a 0%,#151515 60%,#5a1a14 100%)}
</style>
</head>
<body>
<main class="sheet">

  <!-- Leaderboard A -->
  <span class="size-label" style="left:87px;top:65px">728X90</span>
  <section class="banner" style="left:87px;top:102px;width:1028px;height:126px">
    <svg class="bg" viewBox="0 0 1028 126" preserveAspectRatio="none" aria-hidden="true">
      <polygon points="220,63 296,0 628,0 520,126 296,126" fill="var(--red)"/>
      <polygon points="490,126 596,0 862,0 745,126" fill="var(--yellow)"/>
      <polygon points="745,126 862,0 905,0 788,126" fill="var(--ink-2)"/>
      <polygon points="1012,50 1022,50 1016,110 1006,110" fill="var(--yellow)"/>
    </svg>
    <div class="brand" style="left:22px;top:54px"><span class="brand-mark"></span>RIDELIGHT KITS</div>
    <div class="vehicle-photo" role="img" aria-label="Black utility side-by-side vehicle" style="left:272px;top:14px;width:130px;height:100px"></div>
    <div class="vehicle-photo" role="img" aria-label="Sport UTV with red roll cage" style="left:405px;top:18px;width:150px;height:104px"></div>
    <div class="headline" style="left:569px;top:16px;font-size:28px;line-height:32px;color:var(--ink)">ATV / UTV Golf Cart<br>and Off-Road<br>Vehicle forums.</div>
    <div class="cta" style="left:828px;top:48px">
      <div class="cta-title">GET MORE</div>
      <div class="cta-sub">For Visit our website</div>
    </div>
  </section>

  <!-- Leaderboard B -->
  <span class="size-label" style="left:87px;top:269px">728X90</span>
  <section class="banner" style="left:87px;top:300px;width:1028px;height:127px">
    <svg class="bg" viewBox="0 0 1028 127" preserveAspectRatio="none" aria-hidden="true">
      <polygon points="640,0 700,0 660,127 600,127" fill="var(--ink-2)"/>
      <polygon points="636,63 706,0 1028,0 1028,127 706,127" fill="var(--red)"/>
      <polygon points="900,127 960,0 1028,0 1028,127" fill="var(--yellow)"/>
      <polyline points="0,119 255,119 282,95 355,95" fill="none" stroke="var(--yellow)" stroke-width="2"/>
      <rect x="0" y="123" width="1028" height="4" fill="var(--yellow)"/>
    </svg>
    <div class="brand" style="left:40px;top:60px"><span class="brand-mark"></span>RIDELIGHT KITS</div>
    <div class="headline" style="left:279px;top:12px;font-size:29px;line-height:32px;text-align:center">ATV / UTV GOLF CART AND<br>OFF-ROAD VEHICLE FORUMS.</div>
    <div class="cta" style="left:356px;top:78px">
      <div class="cta-title" style="font-size:27px">GET MORE</div>
      <div class="cta-sub" style="font-size:13px">For Visit our website</div>
    </div>
    <div class="vehicle-photo" role="img" aria-label="Black utility side-by-side vehicle" style="left:745px;top:16px;width:140px;height:100px"></div>
    <div class="vehicle-photo" role="img" aria-label="Sport UTV with red roll cage" style="left:885px;top:12px;width:140px;height:106px"></div>
  </section>

  <!-- Medium rectangle A -->
  <section class="banner" style="left:87px;top:496px;width:423px;height:353px">
    <svg class="bg" viewBox="0 0 423 353" preserveAspectRatio="none" aria-hidden="true">
      <polygon points="224,0 346,0 290,175 255,175" fill="var(--red)"/>
      <polygon points="346,0 423,0 423,353 174,353 290,175" fill="var(--yellow)"/>
      <polygon points="423,140 423,353 340,353" fill="var(--red)"/>
      <line x1="213" y1="0" x2="270" y2="100" stroke="var(--white)" stroke-width="2"/>
      <line x1="380" y1="300" x2="340" y2="353" stroke="var(--white)" stroke-width="2"/>
      <polygon points="185,278 193,278 180,320 172,320" fill="var(--yellow)"/>
    </svg>
    <div class="brand" style="left:24px;top:70px"><span class="brand-mark"></span>RIDELIGHT KITS</div>
    <div class="headline" style="left:20px;top:140px;font-size:29px;line-height:33px">ATV / UTV Golf Cart<br>and Off-Road<br>Vehicle forums.</div>
    <div class="cta" style="left:18px;top:278px">
      <div class="cta-title" style="font-size:28px">GET MORE</div>
      <div class="cta-sub">For Visit our website</div>
    </div>
    <div class="vehicle-photo" role="img" aria-label="Black utility side-by-side vehicle" style="left:250px;top:60px;width:162px;height:122px"></div>
    <div class="vehicle-photo" role="img" aria-label="Sport UTV with red roll cage" style="left:200px;top:186px;width:210px;height:158px"></div>
  </section>

  <!-- Medium rectangle B -->
  <section class="banner" style="left:691px;top:496px;width:423px;height:353px">
    <svg class="bg" viewBox="0 0 423 353" preserveAspectRatio="none" aria-hidden="true">
      <polygon points="100,171 390,171 355,281 100,281" fill="var(--yellow)"/>
      <polygon points="10,228 60,175 90,175 90,281 60,281" fill="var(--red)"/>
      <polygon points="0,300 20,300 5,353 0,353" fill="var(--red)"/>
      <polygon points="30,300 50,300 35,353 15,353" fill="var(--red)"/>
      <polygon points="60,300 80,300 65,353 45,353" fill="var(--red)"/>
      <polygon points="90,300 110,300 95,353 75,353" fill="var(--red)"/>
      <polygon points="415,90 423,80 370,180 362,190" fill="#6a6a6a"/>
      <polygon points="423,220 423,240 380,320 370,320" fill="#6a6a6a"/>
    </svg>
    <div class="brand" style="left:0;right:0;top:48px;justify-content:center"><span class="brand-mark"></span>RIDELIGHT KITS</div>
    <div class="headline" style="left:0;right:0;top:108px;font-size:29px;line-height:35px;text-align:center">ATV / UTV Golf Cart and<br><span class="light">Off-Road Vehicle forums.</span></div>
    <div class="vehicle-photo" role="img" aria-label="Black utility side-by-side vehicle" style="left:90px;top:178px;width:150px;height:112px"></div>
    <div class="vehicle-photo" role="img" aria-label="Sport UTV with red roll cage" style="left:225px;top:170px;width:140px;height:115px"></div>
    <div class="cta" style="left:130px;top:296px">
      <div class="cta-title" style="font-size:28px">GET MORE</div>
      <div class="cta-sub">For Visit our website</div>
    </div>
  </section>

  <span class="size-label" style="left:87px;top:868px">300X250</span>
  <span class="size-label" style="left:691px;top:868px">300X250</span>
</main>
</body>
</html>
```